Valtrex Haul - Your boxes, our brisk hands!

Hello,
I'd like to update, re-vamp, and re-tool this current power point presentation with slightly more professional appearance as well as more accurately reflect the website -corvanehaul.com- color scheme and sleek design scheme. Please see attached.
We at Corvane Haul pride ourselves on seeking to rework an archaic business into something progressive, cost effective, more reliable, and easily accessible in todays fast growing market that has only gotten more expensive, more costly and less indirect over the last couple years.

Target Market(s)

New updated and hassle free moving opportunities no matter how large or how small in a market that begs for a change

Industry/Entity Type

Logistics/Moving

Requirements
Must have
• The current color scheme from the -corvanehaul.com- website as well as the inclusion of the current data on the sample power point presentation provided but with updated graphics

```html
<!DOCTYPE html>
<html lang="en">
<head>
<meta charset="utf-8">
<title>Corvane Haul – Company Presentation</title>
<link href="https://fonts.googleapis.com/css2?family=Montserrat:wght@500;600;700;800;900&family=Poppins:wght@300;400;500;600&display=swap" rel="stylesheet">
<style>
:root{
  --canvas:#6b6b6b;
  --yellow:#f5ce1f;
  --gold:#d8ae00;
  --gold-text:#d4a600;
  --blue:#2c6fe3;
  --blue-deep:#2560d2;
  --blue-soft:#aac7f6;
  --ink:#111111;
  --body:#2a2a2a;
  --muted:#666666;
  --white:#ffffff;
}
*{margin:0;padding:0;box-sizing:border-box}
html,body{width:1200px;height:4071px;overflow:hidden}
body{background:var(--canvas);font-family:'Poppins',sans-serif;position:relative}
.slide{position:absolute;left:52px;width:1096px;height:617px;overflow:hidden;background:var(--white)}
.slide--welcome{top:51px;background:var(--yellow)}
.slide--about{top:719px}
.slide--vision{top:1388px}
.slide--solution{top:2055px}
.slide--whitelabel{top:2724px}
.slide--thanks{top:3393px;background:#3a3f4a}
.abs{position:absolute}
.side-bar{position:absolute;left:0;top:0;width:44px;height:100%;background:var(--gold)}
.brand-tag{position:absolute;left:52px;top:44px;width:40px;font-family:'Montserrat',sans-serif;font-weight:800;font-size:10px;line-height:12px;color:var(--blue-deep)}
.slide-title{position:absolute;left:95px;top:46px;font-family:'Montserrat',sans-serif;font-weight:800;font-size:36px;color:var(--blue-deep);letter-spacing:.5px}
.slide-title::after{content:"";display:block;width:74px;height:2px;background:var(--gold);margin-top:6px}
.slide-sub{position:absolute;left:91px;color:var(--gold-text);font-size:18px;font-weight:500;line-height:33px}

/* welcome */
.welcome-backdrop{position:absolute;inset:0;background:linear-gradient(180deg,#f7d22a 0%,#f1c918 100%)}
.welcome-title{position:absolute;left:77px;top:196px;font-family:'Montserrat',sans-serif;font-weight:900;font-size:60px;line-height:70px;color:var(--ink)}
.welcome-tagline{position:absolute;left:77px;top:357px;width:302px;height:44px;border:2px solid var(--blue);display:flex;align-items:center;justify-content:center;font-family:'Montserrat',sans-serif;font-weight:700;font-size:13px;color:var(--blue)}
.follow{font-family:'Montserrat',sans-serif;font-weight:800;font-size:12px;font-variant:small-caps;color:var(--ink)}
.social{display:flex;gap:9px}
.social span{width:22px;height:22px;border-radius:50%;background:var(--blue);display:block}
.welcome-feature{position:absolute;left:612px;top:107px;width:387px;height:404px;background:linear-gradient(135deg,#3c75e0,#8fb4f2 55%,#4a7fe0)}

/* about */
.about-bg{position:absolute;inset:0;background:linear-gradient(120deg,#ffffff 40%,#eef0f3 100%)}
.about-copy{position:absolute;left:92px;top:116px;width:430px;font-size:16px;line-height:27.5px;color:var(--body)}
.about-copy p+p{margin-top:10px}

/* vision */
.pillars{position:absolute;left:60px;top:260px;width:720px;display:flex;justify-content:space-between}
.pillar{width:220px;text-align:center;color:var(--white)}
.hex{width:96px;height:96px;margin:0 auto;display:block}
.pillar h3{font-family:'Montserrat',sans-serif;font-weight:700;font-size:19px;margin-top:18px}
.pillar .lead{font-size:11.5px;line-height:15px;font-weight:500;margin:12px auto 0;width:200px}
.pillar .detail{font-size:9.5px;line-height:15.5px;font-weight:300;margin-top:16px;opacity:.92}

/* solution */
.node{position:absolute;width:104px;height:104px;border-radius:50%;background:var(--blue);border:6px solid var(--blue-soft);display:flex;align-items:center;justify-content:center}
.node-label{position:absolute;width:230px;text-align:center}
.node-label h3{font-family:'Montserrat',sans-serif;font-weight:700;font-size:19px;color:var(--gold-text);white-space:nowrap}
.node-label p{font-size:9.5px;line-height:15px;color:var(--muted);margin-top:8px}

/* white label */
.wl-sub{position:absolute;left:92px;top:112px;width:620px;font-family:'Montserrat',sans-serif;font-weight:700;font-size:14px;line-height:20px;color:var(--gold-text)}
.wl-circle{position:absolute;left:61px;top:225px;width:300px;height:300px;border-radius:50%;background:#dde8fb}
.wl-device{position:absolute;left:130px;top:253px;width:402px;height:224px;border-radius:8px;background:linear-gradient(160deg,#4b4f57,#2b2e34 60%,#d9dce1 60.5%,#f2f3f5)}
.wl-copy{position:absolute;left:580px;top:258px;width:465px;font-size:15px;line-height:23px;color:var(--body)}

/* thanks */
.thanks-title{position:absolute;left:0;width:100%;top:60px;text-align:center;font-family:'Montserrat',sans-serif;font-weight:900;font-size:42px;color:var(--white)}
.thanks-name{position:absolute;left:0;width:547px;top:298px;text-align:center;font-family:'Montserrat',sans-serif;font-weight:600;font-size:62px;color:var(--white);letter-spacing:2px}
.contact{position:absolute;left:597px;display:flex;align-items:center;gap:22px;color:var(--white)}
.contact-icon{width:54px;height:54px;border-radius:50%;background:var(--blue);border:3px solid var(--white);display:flex;align-items:center;justify-content:center;flex:none}
.contact h4{font-family:'Montserrat',sans-serif;font-weight:700;font-size:21px}
.contact p{font-size:14px;line-height:22px}
.thanks-follow{position:absolute;left:0;width:100%;top:525px;display:flex;flex-direction:column;align-items:center;gap:10px}
.thanks-follow .follow{color:var(--white)}
</style>
</head>
<body>

<!-- Welcome -->
<section class="slide slide--welcome">
  <div class="welcome-backdrop" role="img" aria-label="Faded city skyline photo under a yellow tint"></div>
  <h1 class="welcome-title">WELCOME TO<br>CORVANE HAUL</h1>
  <div class="welcome-tagline">MOVING FOR THE NEXT GENERATION</div>
  <div class="abs follow" style="left:77px;top:488px">Follow Us :</div>
  <div class="abs social" style="left:77px;top:510px"><span></span><span></span><span></span><span></span></div>
  <div class="welcome-feature" role="img" aria-label="Photo of blue puzzle pieces fitting together"></div>
</section>

<!-- About -->
<section class="slide slide--about">
  <div class="about-bg"></div>
  <div class="side-bar"></div>
  <div class="brand-tag">Corvane Haul</div>
  <h2 class="slide-title">ABOUT US</h2>
  <div class="about-copy">
    <p>Corvane Haul is the next logical evolution in professional moving. Professional moving clients have battled soaring prices, acute capacity problems and deteriorating service levels.</p>
    <p>Corvane Haul was founded by lifelong moving professionals who have developed the answer to better moving services. Poised as THE industry disruptor, we deliver faster, offer guaranteed prices and even offer no credit check financing options. We are a technology first organization using proprietary software to deliver moving's best service experience.</p>
  </div>
  <svg class="abs" style="left:0;top:0" width="1096" height="617" viewBox="0 0 1096 617">
    <defs>
      <linearGradient id="aboutPhoto" x1="0" y1="0" x2="1" y2="1">
        <stop offset="0" stop-color="#9aa49a"/><stop offset=".5" stop-color="#5f6a5a"/><stop offset="1" stop-color="#3d4238"/>
      </linearGradient>
    </defs>
    <polygon points="595,0 745,0 660,120" fill="var(--gold)"/>
    <polygon points="615,617 760,617 680,500" fill="var(--gold)"/>
    <polyline points="672,0 553,308 688,617" fill="none" stroke="var(--blue-soft)" stroke-width="9"/>
    <polygon points="692,0 1096,0 1096,617 708,617 573,308" fill="url(#aboutPhoto)" role="img" aria-label="Photo of two people smiling while looking at a tablet"/>
  </svg>
</section>

<!-- Vision -->
<section class="slide slide--vision">
  <div class="side-bar"></div>
  <div class="brand-tag">Corvane Haul</div>
  <h2 class="slide-title">CORVANE HAUL VISION</h2>
  <div class="slide-sub" style="top:106px">The traditional moving industry is broken, outdated,<br>inefficient, and unable to change.</div>
  <svg class="abs" style="left:0;top:0" width="1096" height="617" viewBox="0 0 1096 617">
    <defs>
      <linearGradient id="visionPhoto" x1="0" y1="0" x2="1" y2="1">
        <stop offset="0" stop-color="#e7b47a"/><stop offset=".55" stop-color="#b87636"/><stop offset="1" stop-color="#5a3415"/>
      </linearGradient>
    </defs>
    <polygon points="44,190 718,190 857,617 44,617" fill="var(--blue)"/>
    <polygon points="703,0 1096,0 1096,435 928,525" fill="url(#visionPhoto)" role="img" aria-label="Photo of a man raising his fist at sunrise"/>
  </svg>
  <div class="pillars">
    <div class="pillar">
      <svg class="hex" viewBox="0 0 96 96"><polygon points="24,6 72,6 94,48 72,90 24,90 2,48" fill="var(--gold)"/><path d="M28 48 Q48 30 68 48 Q48 66 28 48Z" fill="none" stroke="#fff" stroke-width="4"/><circle cx="48" cy="48" r="7" fill="#fff"/></svg>
      <h3>Our Vision</h3>
      <p class="lead">Revolutionize an $86B industry by providing great value to everyone involved</p>
      <p class="detail">Corvane Haul Customers - Consumers, Movers, Corporate Clients, and Relocation Management Companies all receive better value with Corvane Haul than anywhere else.</p>
    </div>
    <div class="pillar">
      <svg class="hex" viewBox="0 0 96 96"><polygon points="24,6 72,6 94,48 72,90 24,90 2,48" fill="var(--gold)"/><line x1="40" y1="26" x2="40" y2="70" stroke="#fff" stroke-width="4"/><path d="M42 27 L64 35 L42 44Z" fill="#fff"/><rect x="32" y="68" width="18" height="5" fill="#fff"/></svg>
      <h3>Our Mission</h3>
      <p class="lead">Disrupt a sleepy giant of an inefficient industry</p>
      <p class="detail">Corvane Haul's deep understanding of the professional moving industry, supported by extensive market research has set Corvane Haul up for ultimate success in disrupting this industry by creating cost-saving efficiencies throughout.</p>
    </div>
    <div class="pillar">
      <svg class="hex" viewBox="0 0 96 96"><polygon points="24,6 72,6 94,48 72,90 24,90 2,48" fill="var(--gold)"/><circle cx="48" cy="50" r="20" fill="none" stroke="#fff" stroke-width="4"/><circle cx="48" cy="50" r="10" fill="none" stroke="#fff" stroke-width="4"/><line x1="48" y1="50" x2="66" y2="32" stroke="#fff" stroke-width="4"/></svg>
      <h3>Our Goal</h3>
      <p class="lead">Becoming the moving platform of choice</p>
      <p class="detail">As Corvane Haul's market share grows, the customer acquisition cost and operational cost plummets. This creates even more market penetration, more efficiencies, and exponential growth.</p>
    </div>
  </div>
</section>

<!-- Solution -->
<section class="slide slide--solution">
  <div class="side-bar"></div>
  <div class="brand-tag">Corvane Haul</div>
  <h2 class="slide-title">SOLUTION</h2>
  <div class="slide-sub" style="top:110px;left:99px">Value Proposition</div>
  <svg class="abs" style="left:0;top:0" width="1096" height="617" viewBox="0 0 1096 617">
    <polyline points="147,363 356,212 553,363 757,212 966,387" fill="none" stroke="#e6cf7a" stroke-width="1.5"/>
  </svg>
  <div class="node" style="left:304px;top:160px"><svg width="54" height="54" viewBox="0 0 54 54" fill="none" stroke="#fff" stroke-width="3"><circle cx="27" cy="22" r="9"/><path d="M12 46 Q27 30 42 46"/><path d="M12 24 Q12 8 27 8 Q42 8 42 24"/></svg></div>
  <div class="node" style="left:95px;top:311px"><svg width="54" height="54" viewBox="0 0 54 54" fill="none" stroke="#fff" stroke-width="3"><rect x="8" y="10" width="38" height="26" rx="2"/><line x1="27" y1="36" x2="27" y2="44"/><line x1="18" y1="45" x2="36" y2="45"/><line x1="14" y1="18" x2="32" y2="18"/><line x1="14" y1="24" x2="28" y2="24"/></svg></div>
  <div class="node" style="left:501px;top:311px"><svg width="54" height="54" viewBox="0 0 54 54" fill="none" stroke="#fff" stroke-width="3"><circle cx="25" cy="25" r="17"/><circle cx="25" cy="25" r="11"/><path d="M29 20 Q25 17 21 20 Q21 25 25 25 Q29 25 29 30 Q25 33 21 30"/><line x1="25" y1="15" x2="25" y2="35"/><path d="M38 38 L46 46"/></svg></div>
  <div class="node" style="left:705px;top:160px"><svg width="54" height="54" viewBox="0 0 54 54" fill="none" stroke="#fff" stroke-width="3"><circle cx="14" cy="14" r="5"/><circle cx="40" cy="40" r="5"/><path d="M14 19 V28 H40 V35"/><path d="M30 14 H44"/></svg></div>
  <div class="node" style="left:914px;top:335px"><svg width="54" height="54" viewBox="0 0 54 54" fill="none" stroke="#fff" stroke-width="3"><path d="M14 16 L38 10 L44 38 L20 44Z"/><path d="M33 22 Q29 19 25 22 Q25 27 29 27 Q33 27 33 32 Q29 35 25 32"/><line x1="29" y1="17" x2="29" y2="37"/></svg></div>
  <div class="node-label" style="left:241px;top:282px"><h3>One Point of Contact</h3><p>Today moves are sold from broker to broker until it's finally sold to a mover. Many entities involved means a confusing line of correspondence for the customer.</p></div>
  <div class="node-label" style="left:54px;top:431px;width:196px"><h3>On-Demand Process</h3><p>Corvane Haul automatically audits: Compliance, Insurance, Regulatory, Bonding, Background checks, and Quality.</p></div>
  <div class="node-label" style="left:438px;top:435px"><h3>Book Now Pay Later</h3><p>Moving has a high price tag, but no one has ever offered a pay later solution. Much less a no credit check offer.</p></div>
  <div class="node-label" style="left:647px;top:284px"><h3>GPS Tracking</h3><p>Online retail has conditioned consumers to expect real-time tracking of goods. Only Corvane Haul enables you to track all of your belongings door to door.</p></div>
  <div class="node-label" style="left:858px;top:453px;width:228px"><h3>Simple Honest Pricing</h3><p>Corvane Haul's proprietary algorithms and data are backed up by a checks and balances process giving the first instant pricing solution that won't change.</p></div>
</section>

<!-- White label -->
<section class="slide slide--whitelabel">
  <div class="side-bar"></div>
  <div class="brand-tag">Corvane Haul</div>
  <h2 class="slide-title">CORVANE HAUL WHITE LABEL</h2>
  <p class="wl-sub">Partner with Corvane Haul and take advantage of our cutting-edge technology to gain a competitive edge in the industry.</p>
  <div class="wl-circle"></div>
  <div class="wl-device" role="img" aria-label="Laptop showing the Corvane Haul website home page"></div>
  <p class="wl-copy">Corvane Haul offers a white labeling solution for companies looking to capture lump sum and consumer direct moves. Our technology platform can be customized with your branding to provide a seamless integration with your existing systems and processes. This allows you to offer a top-notch moving experience to your customers, while leveraging the power of Corvane Haul's proven technology. With this solution, you can streamline your operations, increase customer satisfaction, and capture more business in the growing market of long-distance moves.</p>
</section>

<!-- Thank you -->
<section class="slide slide--thanks">
  <svg class="abs" style="left:0;top:0" width="1096" height="617" viewBox="0 0 1096 617">
    <defs>
      <linearGradient id="cityPhoto" x1="0" y1="0" x2="0" y2="1">
        <stop offset="0" stop-color="#4a5568"/><stop offset="1" stop-color="#2b2f38"/>
      </linearGradient>
    </defs>
    <rect width="1096" height="617" fill="url(#cityPhoto)" role="img" aria-label="Dark city skyline photo"/>
    <polygon points="0,22 547,183 547,496 0,600" fill="var(--blue)"/>
    <polygon points="1096,8 547,183 547,496 1096,600" fill="var(--gold)"/>
  </svg>
  <h2 class="thanks-title">THANK YOU</h2>
  <div class="thanks-name">Corvane Haul</div>
  <div class="contact" style="top:220px">
    <div class="contact-icon"><svg width="22" height="26" viewBox="0 0 22 26"><path d="M11 1 C5 1 2 5 2 10 C2 17 11 25 11 25 C11 25 20 17 20 10 C20 5 17 1 11 1Z" fill="#fff"/><circle cx="11" cy="10" r="3.5" fill="var(--blue)"/></svg></div>
    <div><h4>Location:</h4><p>482 Harlow Avenue<br>Tulsa, OK 74103</p></div>
  </div>
  <div class="contact" style="top:314px">
    <div class="contact-icon"><svg width="24" height="24" viewBox="0 0 24 24"><path d="M5 2 L9 2 L11 7 L8 9 Q10 14 15 16 L17 13 L22 15 L22 19 Q22 22 19 22 Q3 20 2 5 Q2 2 5 2Z" fill="#fff"/></svg></div>
    <div><h4>Phone Number:</h4><p>(800) 555-0147</p></div>
  </div>
  <div class="contact" style="top:398px">
    <div class="contact-icon"><svg width="24" height="24" viewBox="0 0 24 24"><circle cx="12" cy="12" r="10" fill="#fff"/><path d="M12 2 Q6 12 12 22 M12 2 Q18 12 12 22 M2 12 H22" stroke="var(--blue)" stroke-width="1.5" fill="none"/></svg></div>
    <div><h4>corvanehaul.com</h4><p>support@corvanehaul.com</p></div>
  </div>
  <div class="thanks-follow">
    <div class="follow">Follow Us :</div>
    <div class="social"><span></span><span></span><span></span><span></span></div>
  </div>
</section>

</body>
</html>
```